design a beautiful, neat and professional looking 10 page templete for an online course

I designed an online course. It about the newborn adoption process. I need you to design the template for it. Just the first 10 pages is enough. I'm thinking a neutral palette with a pop of a minor color to keep it from being boring. The pop of color should not distract the reader. You can design how you want. If you want to add small details or hearts or a shape in background you can. Just dont overdo it. Sparingly is the key. You can make pages a different color. It just needs to look like a neutral color palette with a small pop of color.
Updates

Low design quality

Target Market(s)

people who are adopting a newborn in the USA

Industry/Entity Type

newborn adoption

Font styles to use
Sans Serif

Colors

Designer to choose colors to be used in the design.

Requirements
Should not have
• bold or distracting colors or patterns

```html
<!DOCTYPE html>
<html lang="en">
<head>
<meta charset="utf-8">
<title>Newborn Adoption Course Template</title>
<link href="https://fonts.googleapis.com/css2?family=Nunito:wght@400;600;800;900&family=Barlow:wght@400&display=swap" rel="stylesheet">
<style>
  :root{
    --bg:#e9f595;
    --sand:#f3e8da;
    --clay:#e8d5c4;
    --mist:#e1e8e3;
    --accent:#c9755b;
    --taupe:#b39a86;
    --sage:#93aa9c;
    --rose:#d6a18f;
    --navy:#2a2d4a;
    --title:#5b6f8f;
    --cream:#fbf7f2;
    --white:#ffffff;
    --grey:#77737a;
    --photo-a:#eadbd0;
    --photo-b:#ebe6e2;
  }
  html,body{margin:0;padding:0;width:1200px;height:1200px;overflow:hidden;background:var(--bg);}
  .board{position:relative;width:1200px;height:1200px;font-family:"Nunito",sans-serif;}
  .slide{position:absolute;display:block;filter:drop-shadow(0 14px 14px rgba(90,110,40,.3));}
  .promo{position:absolute;left:475px;top:64px;font-family:"Barlow",sans-serif;font-size:27.5px;line-height:36px;color:#111;letter-spacing:.4px;}
  .slide text{font-family:"Nunito",sans-serif;}
  .lb{font-size:5px;font-weight:800;fill:var(--accent);letter-spacing:.4px;}
  .h{font-size:13px;font-weight:900;fill:var(--navy);}
  .p{font-size:5.4px;font-weight:600;fill:var(--grey);}
  .t{font-size:6.8px;font-weight:900;fill:var(--navy);}
  .n{font-size:5px;font-weight:800;fill:var(--white);}
  .stat{font-size:9px;font-weight:900;fill:var(--accent);}
  .big{font-size:13px;font-weight:900;fill:var(--white);}
  .sm{font-size:4.6px;font-weight:800;fill:var(--white);}
  .mid{text-anchor:middle;}
</style>
</head>
<body>
<div class="board">

  <div class="promo">Source files available in : power point template<br>with animation and pdf (&nbsp; high resolution )<br>for printing need,<br>i will support to put content in here template<br>and unlimited revision</div>

  <!-- Cover -->
  <svg class="slide" style="left:81px;top:55px" width="328" height="202" viewBox="0 0 528 325">
    <defs><linearGradient id="ph" x1="0" y1="0" x2="1" y2="1"><stop offset="0" stop-color="#dcc6b8"/><stop offset="1" stop-color="#f1ece8"/></linearGradient></defs>
    <rect width="528" height="325" fill="var(--white)"/>
    <path d="M0 0H85C75 25 60 48 30 58C12 64 4 70 0 78Z" fill="var(--sand)"/>
    <path d="M0 212C90 200 160 240 270 252C370 262 450 232 528 196V325H0Z" fill="var(--clay)"/>
    <text x="50" y="127" style="font-size:34px;font-weight:600;fill:var(--title)">newborn</text>
    <text x="50" y="170" style="font-size:34px;font-weight:600;fill:var(--title)">adoption</text>
    <rect x="248" y="60" width="150" height="190" rx="75" fill="none" stroke="var(--accent)" stroke-width="1"/>
    <rect x="256" y="12" width="154" height="240" rx="77" fill="url(#ph)" role="img" aria-label="Photo of a mother kissing her newborn"/>
    <rect x="371" y="175" width="124" height="126" rx="10" fill="var(--white)"/>
    <rect x="377" y="178" width="112" height="80" rx="6" fill="#e4e1e2" role="img" aria-label="Photo of a smiling baby"/>
    <text x="433" y="281" class="t mid">Title Your Here</text>
  </svg>

  <!-- Introduction -->
  <svg class="slide" style="left:81px;top:277px" width="328" height="202" viewBox="0 0 528 325">
    <rect width="528" height="325" fill="var(--white)"/>
    <path d="M350 0H528V215C490 210 470 160 430 130C380 100 270 105 300 60C315 40 345 30 350 0Z" fill="var(--sand)"/>
    <path d="M0 250C30 245 40 275 70 285C95 292 95 310 85 325H0Z" fill="var(--clay)"/>
    <ellipse cx="380" cy="162" rx="97" ry="108" fill="var(--photo-a)" role="img" aria-label="Photo of a baby in a white towel"/>
    <circle cx="443" cy="252" r="38" fill="var(--accent)"/>
    <text x="443" y="253" class="mid" style="font-size:12px;font-weight:900;fill:#fff">100%</text>
    <text x="443" y="265" class="sm mid">Quality</text>
    <text x="52" y="68" class="lb">ABOUT US</text>
    <text x="52" y="90" class="h">Introduction</text>
    <text class="p"><tspan x="52" y="122">Lorem ipsum dolor sit amet, consecte pricing turasanu</tspan><tspan x="52" y="135">adipiscing elit, sed dolor sita huasa eiusmod tempor</tspan><tspan x="52" y="148">incididunt ut labore et dolore magna its aliqual orci eu</tspan><tspan x="52" y="161">lobortis it elementum nibu eiusmod special. Lorem ipsum</tspan><tspan x="52" y="174">dolor sit amet, consecte pricing turasanu adipiscing elit,</tspan><tspan x="52" y="187">sed dolor sita huasa eiusmod tempor Lorem ipsum dolor sit</tspan><tspan x="52" y="200">amet, consecte pricing turasanu adipiscing elit, sed dolor</tspan><tspan x="52" y="213">sita huasa eiusmod tempor incididunt ut labore et dolore</tspan><tspan x="52" y="226">magna its aliqual orci eu lobortis it elementum nibu</tspan><tspan x="52" y="239">eiusmod special. Lorem ipsum dolor sit amet, consecte</tspan><tspan x="52" y="252">pricing turasanu adipiscing elit,</tspan></text>
  </svg>

  <!-- Our Services -->
  <svg class="slide" style="left:437px;top:302px" width="328" height="184" viewBox="0 0 527 296">
    <rect width="527" height="296" fill="var(--white)"/>
    <path d="M270 110C300 70 380 60 440 60C490 60 527 80 527 80V296H300C250 270 240 150 270 110Z" fill="var(--photo-b)" role="img" aria-label="Photo of a sleeping newborn wrapped in a white blanket"/>
    <path d="M0 225C30 220 50 240 70 255C90 270 90 285 80 296H0Z" fill="var(--clay)"/>
    <ellipse cx="373" cy="58" rx="47" ry="33" fill="var(--accent)"/>
    <text x="373" y="61" class="mid" style="font-size:12px;font-weight:900;fill:#fff">2500</text>
    <text x="373" y="71" class="sm mid">Total Newborn</text>
    <text x="41" y="55" class="lb">SERVICES</text>
    <text x="41" y="75" class="h">Our Services</text>
    <text class="p"><tspan x="41" y="102">Lorem ipsum dolor sit amet, consecte pricing turasanu</tspan><tspan x="41" y="114">adipiscing elit, sed dolor sita huasa eiusmod tempor</tspan><tspan x="41" y="126">incididunt ut labore et dolore magna its aliqual orci eu</tspan><tspan x="41" y="138">lobortis it elementum nibu eiusmod special. Lorem</tspan><tspan x="41" y="150">ipsum dolor sit amet, consecte pricing turasanu</tspan><tspan x="41" y="162">adipiscing elit, sed dolor sita huasa eiusmod tempor</tspan></text>
    <text x="41" y="203" class="stat">750+</text><text x="99" y="203" class="stat">150+</text><text x="157" y="203" class="stat">1250+</text>
    <text x="41" y="215" class="t" style="font-size:5.2px">Title Your Here</text><text x="99" y="215" class="t" style="font-size:5.2px">Title Your Here</text><text x="157" y="215" class="t" style="font-size:5.2px">Title Your Here</text>
  </svg>

  <!-- Process -->
  <svg class="slide" style="left:792px;top:302px" width="328" height="184" viewBox="0 0 528 296">
    <rect width="528" height="296" fill="var(--cream)"/>
    <path d="M0 0H70C75 20 65 35 45 35C25 36 15 50 0 65Z" fill="var(--sand)"/>
    <rect x="180" y="30" width="160" height="240" rx="80" fill="none" stroke="var(--accent)" stroke-width="1"/>
    <rect x="188" y="30" width="152" height="235" rx="76" fill="var(--photo-a)" role="img" aria-label="Photo of a sleeping newborn in a blanket"/>
    <text x="36" y="96" class="lb">Process</text>
    <text x="36" y="115" class="h">Title Your Here</text>
    <text class="p"><tspan x="36" y="141">Lorem ipsum dolor sit amet, consecte</tspan><tspan x="36" y="153">pricing turasanu adipiscing elit, sed</tspan><tspan x="36" y="165">dolor sita huasa eiusmod tempor</tspan><tspan x="36" y="177">incididunt ut labore et dolore magna</tspan><tspan x="36" y="189">its aliqual orci eu lobortis it</tspan><tspan x="36" y="201">elementum nibu eiusmod special.</tspan><tspan x="36" y="213">Lorem ipsum dolor sit amet, consecte</tspan><tspan x="36" y="225">pricing turasanu adipiscing elit, sed</tspan><tspan x="36" y="237">dolor sita huasa eiusmod tempor</tspan></text>
    <g>
      <circle cx="377" cy="53" r="9" fill="var(--sage)"/><text x="377" y="55" class="n mid">01</text>
      <text x="403" y="50" class="t">Title Your Here</text>
      <text class="p"><tspan x="403" y="62">Lorem ipsum dolor sit amet,</tspan><tspan x="403" y="74">consecte pricing turasanu</tspan><tspan x="403" y="86">adipiscing elit, sed</tspan></text>
      <circle cx="377" cy="134" r="9" fill="var(--accent)"/><text x="377" y="136" class="n mid">02</text>
      <text x="403" y="131" class="t">Title Your Here</text>
      <text class="p"><tspan x="403" y="143">Lorem ipsum dolor sit amet,</tspan><tspan x="403" y="155">consecte pricing turasanu</tspan><tspan x="403" y="167">adipiscing elit, sed</tspan></text>
      <circle cx="377" cy="214" r="9" fill="var(--taupe)"/><text x="377" y="216" class="n mid">03</text>
      <text x="403" y="211" class="t">Title Your Here</text>
      <text class="p"><tspan x="403" y="223">Lorem ipsum dolor sit amet,</tspan><tspan x="403" y="235">consecte pricing turasanu</tspan><tspan x="403" y="247">adipiscing elit, sed</tspan></text>
    </g>
  </svg>

  <!-- Laughter -->
  <svg class="slide" style="left:81px;top:514px" width="328" height="184" viewBox="0 0 528 297">
    <defs><filter id="sh" x="-30%" y="-30%" width="160%" height="160%"><feDropShadow dx="0" dy="4" stdDeviation="5" flood-color="#c9b9ad" flood-opacity=".4"/></filter></defs>
    <rect width="528" height="297" fill="var(--cream)"/>
    <text x="49" y="57" class="lb">SERVICES</text>
    <text x="49" y="76" class="h">Laughter</text>
    <text class="p"><tspan x="49" y="119">Lorem ipsum dolor sit amet, consecte pricing</tspan><tspan x="49" y="131">turasanu adipiscing elit, sed dolor sita huasa</tspan><tspan x="49" y="143">eiusmod tempor incididunt ut labore et dolore</tspan><tspan x="49" y="155">magna its aliqual orci eu lobortis it elementum</tspan><tspan x="49" y="167">nibu eiusmod special. Lorem ipsum dolor sit amet,</tspan><tspan x="49" y="179">consecte pricing turasanu adipiscing elit, sed dolor</tspan><tspan x="49" y="191">sita huasa eiusmod tempor</tspan></text>
    <rect x="46" y="223" width="89" height="22" rx="11" fill="var(--accent)"/>
    <path d="M60 230.5c1 3 3 5 6 6l1.5-1.5 2 1-1 2c-4 0-9-5-9-9l2-1 1 2z" fill="#fff"/>
    <text x="78" y="236" class="sm">Schedule a call</text>
    <g>
      <circle cx="321" cy="88" r="48" fill="#fff" filter="url(#sh)"/><circle cx="259" cy="49" r="14" fill="var(--sage)"/><text x="259" y="51" class="n mid">01</text>
      <text x="321" y="79" class="t mid">Title Your Here</text><text class="p mid"><tspan x="321" y="92">Lorem ipsum dolor sit</tspan><tspan x="321" y="104">amet dolor sit</tspan></text>
      <circle cx="446" cy="88" r="48" fill="#fff" filter="url(#sh)"/><circle cx="385" cy="49" r="14" fill="var(--accent)"/><text x="385" y="51" class="n mid">02</text>
      <text x="446" y="79" class="t mid">Title Your Here</text><text class="p mid"><tspan x="446" y="92">Lorem ipsum dolor sit</tspan><tspan x="446" y="104">amet dolor sit</tspan></text>
      <circle cx="321" cy="224" r="48" fill="#fff" filter="url(#sh)"/><circle cx="259" cy="187" r="14" fill="var(--taupe)"/><text x="259" y="189" class="n mid">03</text>
      <text x="321" y="215" class="t mid">Title Your Here</text><text class="p mid"><tspan x="321" y="228">Lorem ipsum dolor sit</tspan><tspan x="321" y="240">amet dolor sit</tspan></text>
      <circle cx="446" cy="224" r="48" fill="#fff" filter="url(#sh)"/><circle cx="385" cy="187" r="14" fill="var(--rose)"/><text x="385" y="189" class="n mid">04</text>
      <text x="446" y="215" class="t mid">Title Your Here</text><text class="p mid"><tspan x="446" y="228">Lorem ipsum dolor sit</tspan><tspan x="446" y="240">amet dolor sit</tspan></text>
    </g>
  </svg>

  <!-- Providing the Best Service -->
  <svg class="slide" style="left:437px;top:515px" width="328" height="202" viewBox="0 0 527 325">
    <defs><linearGradient id="cr" x1="0" y1="0" x2="0" y2="1"><stop offset="0" stop-color="#fff"/><stop offset=".5" stop-color="#fbf7f2"/><stop offset="1" stop-color="#f8efe6"/></linearGradient></defs>
    <rect width="527" height="325" fill="url(#cr)"/>
    <text x="263" y="30" class="lb mid">SERVICES</text>
    <text x="263" y="51" class="h mid">Providing the Best Service</text>
    <g>
      <rect x="47" y="100" width="94" height="155" rx="47" fill="#fff"/><circle cx="94" cy="150" r="17" fill="var(--sage)"/><text x="94" y="152" class="n mid">01</text>
      <text x="94" y="189" class="t mid">Title Your Here</text><text class="p mid"><tspan x="94" y="204">Lorem ipsum dolor sit</tspan><tspan x="94" y="217">amet dolor sit</tspan></text>
      <rect x="160" y="100" width="94" height="155" rx="47" fill="#fff"/><circle cx="207" cy="150" r="17" fill="var(--accent)"/><text x="207" y="152" class="n mid">02</text>
      <text x="207" y="189" class="t mid">Title Your Here</text><text class="p mid"><tspan x="207" y="204">Lorem ipsum dolor sit</tspan><tspan x="207" y="217">amet dolor sit</tspan></text>
      <rect x="273" y="100" width="94" height="155" rx="47" fill="#fff"/><circle cx="320" cy="150" r="17" fill="var(--taupe)"/><text x="320" y="152" class="n mid">03</text>
      <text x="320" y="189" class="t mid">Title Your Here</text><text class="p mid"><tspan x="320" y="204">Lorem ipsum dolor sit</tspan><tspan x="320" y="217">amet dolor sit</tspan></text>
      <rect x="386" y="100" width="94" height="155" rx="47" fill="#fff"/><circle cx="433" cy="150" r="17" fill="var(--rose)"/><text x="433" y="152" class="n mid">04</text>
      <text x="433" y="189" class="t mid">Title Your Here</text><text class="p mid"><tspan x="433" y="204">Lorem ipsum dolor sit</tspan><tspan x="433" y="217">amet dolor sit</tspan></text>
    </g>
    <text class="p mid"><tspan x="263" y="285">Lorem ipsum dolor sit amet, consecte pricing turasanu adipiscing elit, sed dolor sita huasa eiusmod tempor incididunt ut labore</tspan><tspan x="263" y="298">et dolore magna its aliqual orci eu lobortis it elementum nibu eiusmod special</tspan></text>
  </svg>

  <!-- Timestamp -->
  <svg class="slide" style="left:789px;top:515px" width="331" height="205" viewBox="0 0 532 329">
    <rect width="532" height="329" fill="var(--white)"/>
    <path d="M0 0H100C105 25 85 40 60 40C40 42 35 65 55 75C70 85 40 95 0 90Z" fill="var(--sand)"/>
    <path d="M320 310C380 315 420 300 450 260C480 220 510 240 532 240V329H320Z" fill="var(--clay)"/>
    <text x="53" y="107" class="lb">Timestamp</text>
    <text x="53" y="127" class="h">Title Your Here</text>
    <text class="p"><tspan x="53" y="157">Lorem ipsum dolor sit amet, consecte pricing</tspan><tspan x="53" y="170">turasanu adipiscing elit, sed dolor sita huasa</tspan><tspan x="53" y="183">eiusmod tempor incididunt ut labore et</tspan><tspan x="53" y="196">dolore magna its aliqual orci eu lobortis it</tspan><tspan x="53" y="209">elementum nibu eiusmod special</tspan></text>
    <rect x="50" y="229" width="70" height="20" rx="10" fill="var(--accent)"/>
    <text x="85" y="241" class="sm mid">Title Your Here</text>
    <g>
      <rect x="232" y="22" width="240" height="92" rx="10" fill="#fff" stroke="#f1ece8"/>
      <rect x="243" y="32" width="70" height="72" rx="14" fill="var(--accent)"/>
      <text x="278" y="62" class="big mid">000</text><rect x="258" y="73" width="40" height="14" rx="7" fill="#fff"/><text x="278" y="82" class="mid" style="font-size:5px;font-weight:800;fill:var(--accent)">3 Day</text>
      <text x="331" y="50" class="t">Title Your Here</text><text class="p"><tspan x="331" y="64">Lorem ipsum dolor sit amet, consecte</tspan><tspan x="331" y="77">pricing turasanu adipiscing elit, sed</tspan><tspan x="331" y="90">dolor sita huasa eiusmod</tspan></text>
      <rect x="230" y="120" width="240" height="92" rx="10" fill="#fff" stroke="#f1ece8"/>
      <rect x="241" y="130" width="70" height="72" rx="14" fill="var(--taupe)"/>
      <text x="276" y="160" class="big mid">000</text><rect x="256" y="171" width="40" height="14" rx="7" fill="#fff"/><text x="276" y="180" class="mid" style="font-size:5px;font-weight:800;fill:var(--taupe)">15 Day</text>
      <text x="330" y="148" class="t">Title Your Here</text><text class="p"><tspan x="330" y="162">Lorem ipsum dolor sit amet, consecte</tspan><tspan x="330" y="175">pricing turasanu adipiscing elit, sed</tspan><tspan x="330" y="188">dolor sita huasa eiusmod</tspan></text>
      <rect x="229" y="218" width="240" height="92" rx="10" fill="#fff" stroke="#f1ece8"/>
      <rect x="240" y="228" width="70" height="72" rx="14" fill="var(--sage)"/>
      <text x="275" y="258" class="big mid">000</text><rect x="255" y="269" width="40" height="14" rx="7" fill="#fff"/><text x="275" y="278" class="mid" style="font-size:5px;font-weight:800;fill:var(--sage)">30 Day</text>
      <text x="328" y="246" class="t">Title Your Here</text><text class="p"><tspan x="328" y="260">Lorem ipsum dolor sit amet, consecte</tspan><tspan x="328" y="273">pricing turasanu adipiscing elit, sed</tspan><tspan x="328" y="286">dolor sita huasa eiusmod</tspan></text>
    </g>
  </svg>

  <!-- Information -->
  <svg class="slide" style="left:81px;top:723px" width="328" height="185" viewBox="0 0 528 297">
    <rect width="528" height="297" fill="var(--white)"/>
    <path d="M0 0H255C285 5 295 40 290 80C285 120 300 150 270 190C245 220 150 215 100 200C50 185 40 130 0 120Z" fill="var(--mist)"/>
    <path d="M470 265C480 240 505 240 515 225C522 215 528 215 528 215V297H460C462 285 465 275 470 265Z" fill="var(--sand)"/>
    <path d="M60 60C90 20 160 20 185 60C205 95 195 165 150 195C110 220 55 200 40 160C30 125 40 90 60 60Z" fill="#eddcd9" role="img" aria-label="Photo of a mother holding a baby in a pink blanket"/>
    <path d="M230 72C270 68 315 95 310 150C305 200 250 215 210 205C180 195 178 150 185 120C195 90 205 75 230 72Z" fill="none" stroke="var(--accent)" stroke-width="1"/>
    <circle cx="245" cy="140" r="63" fill="#e6dde2" role="img" aria-label="Photo of a smiling baby"/>
    <circle cx="165" cy="224" r="34" fill="var(--accent)"/>
    <text x="165" y="224" class="mid" style="font-size:12px;font-weight:900;fill:#fff">320</text>
    <text x="165" y="235" class="sm mid">Title Your Here</text>
    <text x="344" y="63" class="lb">ABOUT US</text>
    <text x="344" y="82" class="h">Information</text>
    <text class="p"><tspan x="344" y="106">Lorem ipsum dolor sit amet, consecte pricing</tspan><tspan x="344" y="118">turasanu adipiscing elit, sed dolor sita huasa</tspan><tspan x="344" y="130">eiusmod tempor incididunt ut labore et dolore</tspan><tspan x="344" y="142">magna its aliqual orci eu lobortis it elementum</tspan><tspan x="344" y="154">nibu eiusmod special. Lorem ipsum dolor sit</tspan><tspan x="344" y="166">amet, consecte pricing turasanu adipiscing elit,</tspan><tspan x="344" y="178">sed dolor sita huasa eiusmod tempor</tspan></text>
  </svg>

  <!-- How we work -->
  <svg class="slide" style="left:436px;top:751px" width="329" height="185" viewBox="0 0 529 297">
    <rect width="529" height="297" fill="var(--white)"/>
    <path d="M420 0H529V75C505 80 495 55 475 45C450 35 420 30 420 0Z" fill="var(--sand)"/>
    <path d="M0 220C30 225 45 260 90 270C150 282 250 270 320 297H0Z" fill="var(--clay)"/>
    <rect x="170" y="85" width="359" height="190" rx="30" fill="#fff"/>
    <rect x="50" y="85" width="118" height="188" fill="var(--photo-a)" role="img" aria-label="Photo of a mother with her newborn"/>
    <text x="45" y="33" class="lb">OUR PORTFOLIO</text>
    <text x="45" y="53" class="h">How we work</text>
    <text x="218" y="117" class="t">Title Your Here</text>
    <text class="p"><tspan x="218" y="131">Lorem ipsum dolor sit amet, consecte pricing turasanu adipiscing elit, sed dolor sita huasa</tspan><tspan x="218" y="143">eiusmod tempor incididunt ut labore et dolore magna its</tspan></text>
    <g>
      <circle cx="227" cy="179" r="11" fill="var(--sage)"/><text x="227" y="181" class="n mid">01</text>
      <text x="256" y="168" class="t">Title Your Here</text><text class="p"><tspan x="256" y="181">Lorem ipsum dolor sit amet,</tspan><tspan x="256" y="193">consecte pricing turasanu</tspan></text>
      <circle cx="227" cy="231" r="11" fill="var(--accent)"/><text x="227" y="233" class="n mid">02</text>
      <text x="256" y="220" class="t">Title Your Here</text><text class="p"><tspan x="256" y="233">Lorem ipsum dolor sit amet,</tspan><tspan x="256" y="245">consecte pricing turasanu</tspan></text>
      <circle cx="379" cy="179" r="11" fill="var(--taupe)"/><text x="379" y="181" class="n mid">03</text>
      <text x="408" y="168" class="t">Title Your Here</text><text class="p"><tspan x="408" y="181">Lorem ipsum dolor sit amet,</tspan><tspan x="408" y="193">consecte pricing turasanu</tspan></text>
      <circle cx="379" cy="231" r="11" fill="var(--rose)"/><text x="379" y="233" class="n mid">04</text>
      <text x="408" y="220" class="t">Title Your Here</text><text class="p"><tspan x="408" y="233">Lorem ipsum dolor sit amet,</tspan><tspan x="408" y="245">consecte pricing turasanu</tspan></text>
    </g>
  </svg>

  <!-- Get in touch -->
  <svg class="slide" style="left:792px;top:751px" width="328" height="185" viewBox="0 0 528 297">
    <rect width="528" height="297" fill="var(--white)"/>
    <path d="M0 0H140C145 20 125 35 100 38C70 42 60 60 40 70C25 78 10 75 0 78Z" fill="var(--sand)"/>
    <path d="M320 297C340 270 380 262 420 265C470 268 500 255 528 245V297Z" fill="var(--clay)"/>
    <path d="M220 80C250 40 320 40 345 80C365 115 355 200 330 225C300 255 240 250 215 225C190 195 195 115 220 80Z" fill="var(--photo-b)" role="img" aria-label="Photo of a newborn's feet with a hospital band"/>
    <path d="M140 85C150 65 175 35 188 40C200 46 200 70 215 85C222 98 205 122 180 122C150 122 132 105 140 85Z" fill="var(--accent)"/>
    <text x="186" y="87" class="mid" style="font-size:10px;font-weight:900;fill:#fff">24/7</text>
    <text x="186" y="97" class="sm mid">Customer Service</text>
    <text x="42" y="138" class="lb">CONTACT</text>
    <text x="42" y="156" class="h">Get in touch</text>
    <text class="p"><tspan x="42" y="181">Lorem ipsum dolor sit amet, consecte pricing</tspan><tspan x="42" y="193">turasanu adipiscing elit, sed dolor sita huasa</tspan><tspan x="42" y="205">eiusmod tempor incididunt ut labore et</tspan><tspan x="42" y="217">dolore magna its aliqual orci eu</tspan></text>
    <text x="390" y="83" class="t">Address</text>
    <text class="p"><tspan x="390" y="98">14 Maple Lane, Brookfield, OH,</tspan><tspan x="390" y="110">United States</tspan></text>
    <text x="390" y="139" class="t">Email &amp; Phone</text>
    <text class="p"><tspan x="390" y="153">hello@cradlepath.org</tspan><tspan x="390" y="165">(555) 204 3318</tspan></text>
    <text x="390" y="195" class="t">Website</text>
    <text x="390" y="209" class="p">www.cradlepath.org</text>
  </svg>

  <!-- Title with waves -->
  <svg class="slide" style="left:81px;top:958px" width="328" height="185" viewBox="0 0 528 297">
    <rect width="528" height="297" fill="var(--white)"/>
    <rect width="528" height="140" fill="var(--photo-b)" role="img" aria-label="Photo of a sleeping newborn"/>
    <path d="M0 128C80 118 150 100 220 110C300 122 360 135 430 115C480 100 510 75 528 70V297H0Z" fill="var(--sand)"/>
    <path d="M0 150C70 140 140 135 220 145C300 155 360 160 420 140C480 120 510 95 528 90V297H0Z" fill="var(--clay)"/>
    <path d="M0 175C80 168 150 160 230 168C300 175 360 178 420 160C480 142 510 115 528 110V297H0Z" fill="#fff"/>
    <circle cx="57" cy="211" r="10" fill="var(--accent)"/><text x="57" y="213" class="n mid">01</text>
    <circle cx="174" cy="211" r="10" fill="var(--taupe)"/><text x="174" y="213" class="n mid">02</text>
    <text x="48" y="239" class="t">Title Your Here</text><text class="p"><tspan x="48" y="252">Lorem ipsum dolor sit amet,</tspan><tspan x="48" y="264">consecte pricing</tspan></text>
    <text x="164" y="239" class="t">Title Your Here</text><text class="p"><tspan x="164" y="252">Lorem ipsum dolor sit amet,</tspan><tspan x="164" y="264">consecte pricing</tspan></text>
    <text x="311" y="205" class="h" style="font-size:12px">Title Your Here</text>
    <text class="p"><tspan x="311" y="229">Lorem ipsum dolor sit amet, consecte pricing turasanu</tspan><tspan x="311" y="241">adipiscing elit, sed dolor sita huasa eiusmod tempor</tspan><tspan x="311" y="253">incididunt ut labore et dolore magna its aliqual orci eu</tspan><tspan x="311" y="265">lobortis it elementum nibu eiusmod special.</tspan></text>
  </svg>

  <!-- Visit the website -->
  <svg class="slide" style="left:437px;top:961px" width="328" height="184" viewBox="0 0 528 296">
    <rect width="528" height="296" fill="var(--white)"/>
    <path d="M0 0H310C320 25 300 40 270 42C210 45 185 80 195 130C205 180 140 190 130 230C125 260 150 280 150 296H0Z" fill="var(--clay)"/>
    <path d="M370 296C375 265 400 250 440 245C480 240 510 200 528 185V296Z" fill="var(--sand)"/>
    <rect x="68" y="60" width="164" height="114" rx="6" fill="#3a3a42"/>
    <rect x="73" y="65" width="154" height="102" fill="#e6e9ec" role="img" aria-label="Website preview on a laptop screen"/>
    <path d="M50 174H250L244 180H56Z" fill="#cfd3d8"/>
    <text x="291" y="58" class="lb">MOCKUP</text>
    <text class="h"><tspan x="291" y="77">Visit the Website to</tspan><tspan x="291" y="93">Adoption</tspan></text>
    <text x="291" y="133" class="t">Lorem lipsum dolor sit amet</text>
    <text class="p"><tspan x="291" y="150">Lorem ipsum dolor sit amet, consecte pricing turasanu</tspan><tspan x="291" y="162">adipiscing elit, sed dolor sita huasa eiusmod tempor</tspan><tspan x="291" y="174">incididunt ut labore et dolore magna</tspan></text>
    <rect x="50" y="200" width="200" height="62" rx="8" fill="#fff"/>
    <circle cx="86" cy="231" r="12" fill="var(--sage)"/><text x="86" y="233" class="n mid">01</text>
    <text x="114" y="221" class="t">Lorem lipsum dolor sit amet</text><text class="p"><tspan x="114" y="234">Lorem ipsum dolor sit amet,</tspan><tspan x="114" y="246">consecte pricing turasanu</tspan></text>
    <rect x="276" y="200" width="200" height="62" rx="8" fill="#fff"/>
    <circle cx="312" cy="231" r="12" fill="var(--accent)"/><text x="312" y="233" class="n mid">02</text>
    <text x="340" y="221" class="t">Lorem lipsum dolor sit amet</text><text class="p"><tspan x="340" y="234">Lorem ipsum dolor sit amet,</tspan><tspan x="340" y="246">consecte pricing turasanu</tspan></text>
  </svg>

  <!-- Thank you -->
  <svg class="slide" style="left:792px;top:961px" width="328" height="184" viewBox="0 0 528 296">
    <rect width="528" height="296" fill="var(--white)"/>
    <path d="M0 0H175C195 15 190 45 160 55C130 65 110 60 85 80C60 100 30 90 0 95Z" fill="var(--sand)"/>
    <path d="M435 0H528V120C500 100 480 60 450 45C435 37 430 15 435 0Z" fill="var(--clay)"/>
    <rect x="250" y="30" width="230" height="266" fill="var(--photo-b)" role="img" aria-label="Photo of a baby's feet resting in a parent's hand"/>
    <text x="38" y="208" style="font-size:33px;font-weight:900;fill:var(--navy)">Thank You</text>
    <text class="p"><tspan x="40" y="224">Lorem ipsum dolor sit amet, consecte pricing turasanu</tspan><tspan x="40" y="233">adipiscing elit, sed dolor sita huasa</tspan></text>
  </svg>

</div>
</body>
</html>
```